Online Digital Solutions Agency needs a New Business Card

We are a Online/Digital solution agency. We provide WordPress Solutions, Online & Digital Marketing Solutions including SEO, Social Media Marketing and Managed Hosting including VPS and Cloud Hosting solutions. We also design and build bespoke web sites and web applications for various clients. We are very good at site migrations, 3rd party API integrations and mobile app development.

We are rebranding our agency and have already designed a new logo. We have selected 5-6 colours as our base colour and are currently building our new website based around these colour scheme.

Our logo indicates that we are a cloud solution providers, and (i.e. the Clouds), and developers (i.e. HTML Tags, and CSS formats). We use the 5-6 base colours and use various shades of these colours as required.

Our old website is located at: www.brambleforgelabs.com

And our new website is going to be at (we are working on it at the moment ...):
https://creative.brambleforgelabs.co.uk/

Our slogan is "Digital Transformation Specialist"

What we mean by that is; we can take any existing business and get them up and transform them in to the digital world, starting with Hosting, Web Design, Development & Online Marketing aspects.

The powerpoint is a document that we use to present our projects to clients at the moment, and the cloud is on the background as we clarified earlier. (Just to get the idea)

What we are looking for is a Great WoW factor design to start with, ideally with the Logo and Logo colour scheme if possible but not required as long as the designers can do better, and basically give life to our logo and company via the Business card design.

Ideally with some icons perhaps to indicate the address, location, mobile, email, and website would be good but again optional as long as there is a good design.

The cloud can be used as a background if required in a light shade or as a watermark share perhaps.

The logos' and the Illustrator files are shared with you so you can use them as required.

Ideally the business card should have a Name, title, Mobile, Email , Website, Address and perhaps some social media links.

Target Market(s)

New Startups, SME's, Contract and Outsource Clients

Contact Information for Business Card

Company Name:
==============
BrambleForge Labs (UK) Ltd.

Tag Line:
========
“Digital Transformation Specialists”

Adress:
=======

Suite KR73054
14-16 Ashgrove Lane
London
E9 4PD.

Name:
=====
Idris Malek

Title: (Optional)
=============
FQTA, PgD (RNOM)

Role:
=====
Digital Solutions Architect

Email:
=====
idris@brambleforgelabs.uk

WebSite:
=======
http://www.brambleforgelabs.uk

OR

www.brambleforgelabs.uk

Mobile:
======
0044 (0)75 218 30479

OR

+44 (0)75 218 30479

LinkedIN: (Optional)
========
https://uk.linkedin.com/in/idrismalek

Skype: (Optional)
======
idris.malek

Twitter (Optional) : idrismalek

Font styles to use
Serif
Sans Serif

Requirements
Must have
• The Logo
• Business Name
• Person Name
• Title
• Mobile
• Email
• Website
• Address
• I have provided the colour scheme on my files.
Nice to have
• Twiter
• Linked in
• Facebook

```html
<!DOCTYPE html>
<html lang="en">
<head>
<meta charset="utf-8">
<title>BrambleForge Labs – Business Card</title>
<link rel="stylesheet" href="https://fonts.googleapis.com/css2?family=Montserrat:wght@700;800&family=Roboto:wght@400;500;700&display=swap">
<style>
  :root {
    --backdrop: #5e4b3b;
    --card-blue: #1a55a6;
    --card-blue-deep: #15499a;
    --card-blue-light: #3f8fd0;
    --ink-white: #ffffff;
    --ink-muted: #a8c0e2;
    --accent-orange: #f6a623;
    --accent-cyan: #2bb9dc;
    --accent-sky: #9ccbf0;
  }
  * { margin: 0; padding: 0; box-sizing: border-box; }
  html, body { width: 900px; height: 1200px; overflow: hidden; }
  body {
    position: relative;
    background: var(--backdrop);
    font-family: "Roboto", Arial, sans-serif;
    color: var(--ink-white);
  }
  .card {
    position: absolute;
    left: 87px;
    width: 733px;
    height: 428px;
    border-radius: 22px;
    overflow: hidden;
    box-shadow: 0 6px 18px rgba(0,0,0,.35);
  }
  .card--front { top: 126px; background: var(--card-blue); }
  .card--back {
    top: 641px;
    background: radial-gradient(circle at 95% 5%, var(--card-blue-light) 0%, var(--card-blue) 45%, var(--card-blue-deep) 100%);
  }
  .abs { position: absolute; white-space: nowrap; }

  /* identity */
  .identity-bar { left: 50px; top: 55px; width: 7px; height: 73px; background: var(--accent-orange); }
  .person-name { left: 75px; top: 50px; font-size: 27px; font-weight: 700; letter-spacing: .3px; }
  .person-credentials { left: 75px; top: 84px; font-size: 17px; color: var(--ink-muted); }
  .person-role { left: 75px; top: 109px; font-size: 17px; font-weight: 500; color: var(--accent-orange); }

  /* brand */
  .brand { display: flex; align-items: center; gap: 10px; }
  .brand-dot { width: 18px; height: 18px; border-radius: 50%; background: var(--accent-cyan); flex: none; }
  .brand-name { font-family: "Montserrat", Arial, sans-serif; font-weight: 800; color: var(--ink-white); }
  .brand--front { left: 375px; top: 92px; }
  .brand--front .brand-name { font-size: 29px; }
  .brand--back { left: 0; width: 733px; justify-content: center; top: 170px; }
  .brand--back .brand-name { font-size: 40px; }

  .tagline {
    font-family: "Montserrat", Arial, sans-serif;
    font-weight: 700;
    letter-spacing: .2px;
    color: var(--ink-white);
  }
  .tagline .brace { color: var(--accent-sky); font-weight: 400; }
  .tagline .t-orange { color: var(--accent-orange); }
  .tagline .t-cyan { color: var(--accent-cyan); }
  .tagline--front { left: 345px; top: 174px; font-size: 14px; }
  .tagline--back { left: 0; width: 733px; text-align: center; top: 280px; font-size: 15.5px; }

  /* contacts */
  .contact-list { left: 50px; top: 282px; list-style: none; }
  .contact-item { display: flex; align-items: center; height: 26px; font-size: 16px; margin-bottom: 0.5px; }
  .contact-item--gap { margin-top: 2px; }
  .icon-slot { display: inline-flex; align-items: center; color: var(--accent-cyan); font-size: 20px; margin-right: 8px; }
  .icon-slot svg { width: 18px; height: 18px; margin: 0 1px; }
  .social-mark { width: 14px; height: 14px; border-radius: 3px; background: var(--accent-orange); margin: 0 2px; display: inline-block; }
  .contact-spacer { width: 14px; }

  .address { right: 48px; top: 284px; text-align: right; font-size: 16px; line-height: 26px; }
  .address-pin { right: 48px; top: 282px; color: var(--accent-cyan); font-size: 20px; display: inline-flex; align-items: center; }
  .address-pin svg { width: 18px; height: 18px; margin: 0 1px; }
  .address-lines { right: 91px; top: 284px; text-align: right; font-size: 16px; line-height: 26px; }

  /* back web address */
  .web-link {
    left: 0; width: 733px; text-align: center; top: 376px;
    font-family: "Montserrat", Arial, sans-serif; font-weight: 700; font-size: 15px; letter-spacing: 1.6px;
  }
  .web-link .slashes { color: var(--accent-orange); font-size: 24px; font-style: italic; letter-spacing: -2px; margin-right: 10px; vertical-align: -3px; }
  .web-link .w-sky { color: var(--accent-sky); }
  .web-link .w-orange { color: var(--accent-orange); }
</style>
</head>
<body>

<section class="card card--front" aria-label="Business card front">
  <div class="abs identity-bar"></div>
  <div class="abs person-name">Idris Malek</div>
  <div class="abs person-credentials">FQTA, PgD (RNOM)</div>
  <div class="abs person-role">Digital Solutions Architect</div>

  <div class="abs brand brand--front">
    <span class="brand-dot"></span>
    <span class="brand-name">BrambleForge Labs</span>
  </div>
  <div class="abs tagline tagline--front">
    <span class="brace">{</span> <span class="t-orange">DIGITAL</span> : TRANSFORMATION <span class="t-cyan">SPECIALISTS</span> <span class="brace">}</span>
  </div>

  <ul class="abs contact-list">
    <li class="contact-item">
      <span class="icon-slot">{<svg viewBox="0 0 18 18"><rect x="5" y="1.5" width="8" height="15" rx="1.5" fill="none" stroke="#f6a623" stroke-width="1.8"/><circle cx="9" cy="13.5" r="1" fill="#f6a623"/></svg>}</span>
      +44 (0)75 218 30479
    </li>
    <li class="contact-item">
      <span class="icon-slot">{<svg viewBox="0 0 18 18"><rect x="1.5" y="4" width="15" height="10" rx="1" fill="#f6a623"/><path d="M2 4.5 L9 10 L16 4.5" fill="none" stroke="#1a55a6" stroke-width="1.4"/></svg>}</span>
      idris@brambleforgelabs.uk
    </li>
    <li class="contact-item">
      <span class="icon-slot">{<svg viewBox="0 0 18 18" fill="none" stroke="#f6a623" stroke-width="1.4"><circle cx="9" cy="9" r="7"/><ellipse cx="9" cy="9" rx="3" ry="7"/><path d="M2 9h14M3.5 5h11M3.5 13h11"/></svg>}</span>
      www.brambleforgelabs.uk
    </li>
    <li class="contact-item contact-item--gap">
      <span class="icon-slot">{<span class="social-mark"></span>}</span>
      idris.malek
      <span class="contact-spacer"></span>
      <span class="icon-slot">{<span class="social-mark"></span>}{<span class="social-mark"></span>}</span>
      idrismalek
    </li>
  </ul>

  <div class="abs address-lines">
    14-16, Ashgrove Lane<br>
    London, E9 4PD<br>
    United Kingdom
  </div>
  <div class="abs address-pin">{<svg viewBox="0 0 18 18"><path d="M9 1.5c-3 0-5.3 2.3-5.3 5.2 0 3.9 5.3 9.8 5.3 9.8s5.3-5.9 5.3-9.8C14.3 3.8 12 1.5 9 1.5z" fill="#f6a623"/><circle cx="9" cy="6.8" r="2" fill="#1a55a6"/></svg>}</div>
</section>

<section class="card card--back" aria-label="Business card back">
  <div class="abs brand brand--back">
    <span class="brand-dot"></span>
    <span class="brand-name">BrambleForge Labs</span>
  </div>
  <div class="abs tagline tagline--back">
    <span class="brace">{</span> <span class="t-orange">DIGITAL</span> : TRANSFORMATION <span class="t-cyan">SPECIALISTS</span> <span class="brace">}</span>
  </div>
  <div class="abs web-link">
    <span class="slashes">//</span>WWW.BRAMBLE<span class="w-sky">FORGELABS</span><span class="w-orange">.UK</span>
  </div>
</section>

</body>
</html>
```